Design Business Card MAPLE WREN MOWING

We have attached a copy of our Logo, we like a business card designed with logo and mobile phone number on one side that stands out maybe gloss and on the other side it can have the services we do small picture of our logo name number, I have attached an idea to this that I have seen online, this is a business owned by a woman so we like pinks black and navy
Our logo is attached in pdf
Target Market(s)
Home owners that need lawns mowed
Industry/Entity Type
Lawns and gardens
Contact Information for Business Card
Logo business Owner name Deborah Finch mobile number 0491627504
Font styles to use
Look and feel
Each slider illustrates characteristics of the customer's brand and the style your logo design should communicate.

```html
<!DOCTYPE html>
<html lang="en">
<head>
<meta charset="utf-8">
<title>Maple Wren Mowing – Business Card</title>
<link rel="stylesheet" href="https://fonts.googleapis.com/css2?family=Open+Sans:wght@400;600;800&display=swap">
<style>
  :root {
    --bg: #2a2a2e;
    --card: #1d1d20;
    --pink: #ec0a8c;
    --white: #f4f4f4;
    --green: #2fb54a;
    --hex-tone: #2b2b2f;
    --hex-edge: #141416;
  }
  * { margin: 0; padding: 0; box-sizing: border-box; }
  html, body {
    width: 1200px; height: 780px; overflow: hidden;
    background: var(--bg);
    font-family: "Open Sans", Arial, sans-serif;
  }
  .stage {
    position: relative; width: 1200px; height: 780px;
    display: flex; flex-direction: column; align-items: center; justify-content: center; gap: 30px;
  }
  .card {
    position: relative; width: 620px; height: 354px;
    background: var(--card);
    border: 3px solid var(--pink);
    border-radius: 30px;
    overflow: hidden;
    box-shadow: 0 18px 40px rgba(0,0,0,.45);
  }
  /* Front */
  .pattern {
    position: absolute; border-radius: 40px;
    background: radial-gradient(ellipse at center, var(--hex-tone) 0%, var(--hex-tone) 45%, rgba(29,29,32,0) 75%);
  }
  .pattern--top { top: -40px; right: 150px; width: 260px; height: 200px; }
  .pattern--bottom { bottom: -40px; left: 80px; width: 300px; height: 200px; }
  .brand {
    position: absolute; left: 50%; top: 50%; transform: translate(-50%, -50%);
    display: flex; align-items: center; gap: 16px;
  }
  .brand__dot {
    width: 54px; height: 54px; border-radius: 50%; background: var(--pink); flex: none;
  }
  .brand__name {
    color: var(--pink); font-weight: 800; font-size: 38px; line-height: 1.05; letter-spacing: .5px;
  }
  /* Back */
  .contact {
    position: absolute; top: 34px; right: 44px; text-align: right;
  }
  .contact__name { color: var(--pink); font-weight: 800; font-size: 40px; line-height: 1; }
  .contact__phone {
    margin-top: 8px; display: flex; align-items: center; justify-content: flex-end; gap: 10px;
    color: var(--white); font-size: 24px; font-weight: 400;
  }
  .contact__icon { width: 26px; height: 26px; flex: none; }
  .emblem-area {
    position: absolute; right: 50px; top: 140px; width: 210px; height: 180px; border-radius: 50%;
    background: radial-gradient(ellipse at center, #18181a 0%, #1a1a1c 55%, rgba(29,29,32,0) 75%);
  }
  .brand--small {
    left: 40px; top: 44px; transform: none; gap: 10px;
  }
  .brand--small .brand__dot { width: 30px; height: 30px; }
  .brand--small .brand__name { font-size: 22px; }
  .services { position: absolute; left: 40px; bottom: 28px; }
  .services__title { color: var(--pink); font-weight: 800; font-size: 20px; letter-spacing: .5px; margin-bottom: 4px; }
  .services__list { list-style: none; }
  .services__item {
    color: var(--white); font-size: 15px; line-height: 1.45;
    display: flex; align-items: center; gap: 10px;
  }
  .services__item::before {
    content: ""; width: 9px; height: 9px; border-radius: 50%; background: var(--pink); flex: none;
  }
</style>
</head>
<body>
<main class="stage">
  <section class="card card--front">
    <div class="pattern pattern--top" role="img" aria-label="Embossed honeycomb pattern"></div>
    <div class="pattern pattern--bottom" role="img" aria-label="Embossed honeycomb pattern"></div>
    <div class="brand">
      <span class="brand__dot"></span>
      <span class="brand__name">MAPLE WREN<br>MOWING</span>
    </div>
  </section>

  <section class="card card--back">
    <div class="brand brand--small">
      <span class="brand__dot"></span>
      <span class="brand__name">MAPLE WREN<br>MOWING</span>
    </div>
    <div class="contact">
      <p class="contact__name">Deborah</p>
      <p class="contact__phone">0491 627 504
        <svg class="contact__icon" viewBox="0 0 26 26" aria-hidden="true">
          <circle cx="13" cy="13" r="13" fill="var(--green)"/>
          <path d="M8 10.5c0-1 .8-1.8 1.8-1.8h6.4c1 0 1.8.8 1.8 1.8l-1.8 1.2-1.4-1.4h-3.6l-1.4 1.4z M9.5 14h7v3.5h-7z" fill="#fff"/>
        </svg>
      </p>
    </div>
    <div class="emblem-area" role="img" aria-label="Large spot-gloss decorative emblem"></div>
    <div class="services">
      <h2 class="services__title">SERVICES</h2>
      <ul class="services__list">
        <li class="services__item">Garden Maintenance</li>
        <li class="services__item">Hedge Trimming</li>
        <li class="services__item">Trimming</li>
        <li class="services__item">Weeding</li>
        <li class="services__item">Lawn Mowing</li>
      </ul>
    </div>
  </section>
</main>
</body>
</html>
```